Web Design Project

Goal
Combine 2 sites into 1 and enhance functionality

Concept & Overview

My current websites are rowanvoices dot com and tidewaterguides dot org. They are not very popular but I run ads and capture leads and do a tidy bit, but I am going on tour and need to have my website upgrade.

My goal is to redesign rowanvoices and have it as a 10 page site that introduces me and also capture leads in an effective manner then introduce a 5 page system.

I need to update the layout and feel of the site to match the color and image of the book. Currently the book is at tidewaterguides.org and my speaking is at rowanvoices.com. I need the two to combine but I also need functionality to improve. I introduce a 5 step system and I think a visual image like this one can better introduce it.

Here: https://www.brightleafmedia.com/packages/kgt-marla-quinns-life-improvement-program.html

Then in there I need the Lesson Area

Like:

https://www.brightleafmedia.com/packages/kgt-marla-quinns-life-improvement-program.html

They are few samples I can show but this is the main concept.

Target Market(s)

Schools, colleges, churches, and youth organizations

Industry/Entity Type

Tour

Requirements
Must have
• A clean wide home page that is properly designed can do the job of leading to the optin without the sales look.

Nice to have
• https://www.brightleafmedia.com/packages/kgt-marla-quinns-life-improvement-program.html
Should not have
• Sales look and feel

```html
<!DOCTYPE html>
<html lang="en">
<head>
<meta charset="utf-8">
<title>Rowan Whitfield – Youth Speaker</title>
<link href="https://fonts.googleapis.com/css2?family=Pathway+Gothic+One&family=Arimo:wght@400;700&display=swap" rel="stylesheet">
<style>
:root{
  --blue:#2f6db3;
  --blue-dark:#2a63a5;
  --green:#6fba1f;
  --green-light:#8cc84b;
  --ink:#222;
  --muted:#555;
  --grey-bg:#efefef;
  --panel:#f0f0f0;
  --line:#dcdcdc;
  --dark-box:#141414;
  --white:#fff;
}
*{box-sizing:border-box;margin:0;padding:0}
html,body{width:1200px;height:1024px;overflow:hidden;background:var(--white);font-family:"Arimo",Arial,sans-serif;color:var(--ink)}
.wrap{width:800px;margin:0 auto;position:relative}
.display{font-family:"Pathway Gothic One","Arial Narrow",sans-serif;font-weight:400}

.site-header{height:86px;background:linear-gradient(var(--blue),var(--blue-dark))}
.site-title{font-size:44px;color:var(--white);letter-spacing:1px;line-height:86px}

.main-nav{height:52px;background:linear-gradient(#f7f7f7,#e6e6e6);border-bottom:1px solid var(--line)}
.main-nav ul{list-style:none;display:flex;align-items:center;height:52px}
.main-nav li{font-size:11px;font-weight:700;color:#555;text-transform:uppercase}
.main-nav .home{background:var(--green-light);color:var(--white);height:52px;width:136px;display:flex;align-items:center;justify-content:center;position:relative;margin-right:34px}
.main-nav .home::after{content:"";position:absolute;bottom:-7px;left:62px;border:7px solid transparent;border-bottom:0;border-top-color:var(--green-light)}
.main-nav li+li{margin-right:0}
.main-nav .item{margin-right:31px}
.main-nav .item:last-child{margin-right:0;margin-left:auto}

.hero-band{background:var(--grey-bg);padding:16px 0 12px}
.hero-row{display:flex;gap:16px}
.intro{width:546px;height:228px;background:var(--dark-box);border:2px solid #cfcfcf;padding:11px 14px;display:flex;gap:18px;color:var(--white)}
.portrait-col{width:130px}
.portrait{width:130px;height:130px;background:linear-gradient(135deg,#d8d8d8,#5a5a5a)}
.intro-name{font-size:22px;margin-top:8px;letter-spacing:.5px}
.roles{list-style:none;font-size:11px;font-weight:700;margin-top:2px}
.roles li{display:flex;align-items:center;gap:7px;line-height:14px}
.intro-text{flex:1;padding-top:20px}
.quote{font-size:18px;line-height:22px;margin-bottom:12px;word-spacing:2px}
.intro-text p{font-size:10.5px;line-height:12.4px;text-align:justify;margin-bottom:10px}

.video-card{width:238px;background:var(--white);height:228px}
.player{height:156px;background:#111;position:relative}
.player .frame{position:absolute;left:15px;top:8px;width:186px;height:122px;background:linear-gradient(160deg,#6a6f6a,#bca67a 60%,#3b3b3b)}
.player .play{position:absolute;left:89px;top:53px;width:44px;height:30px;border-radius:6px;background:rgba(20,20,20,.8);border:1px solid #666}
.player .side{position:absolute;right:6px;top:6px;display:flex;flex-direction:column;gap:4px}
.player .side span{width:18px;height:16px;background:#2a2a2a;border-radius:2px}
.player .bar{position:absolute;left:0;bottom:0;width:100%;height:20px;background:#000;display:flex;align-items:center;padding:0 8px;gap:10px}
.player .track{flex:1;height:4px;background:#1e7fc1;border-radius:2px;position:relative}
.player .time{position:absolute;right:0;top:-11px;font-size:6px;color:#ccc;background:#333;padding:0 2px}
.video-title{font-size:12px;font-weight:700;margin:8px 8px 8px}
.video-desc{font-size:10.5px;color:var(--muted);line-height:12.4px;margin:0 8px}

.content-row{display:flex;gap:16px;margin-top:16px}
.left-col{width:546px}
.right-col{width:238px}

.book{display:flex;gap:16px;padding:0 12px;height:208px}
.book-art{width:216px;height:188px;background:radial-gradient(circle at 40% 45%,#3d6a9a,#1a2f4c 70%);flex:none}
.book-info h2{font-size:21px;margin-top:-2px}
.isbn{font-size:10.5px;margin:6px 0 18px}
.book-info p{font-size:10.5px;line-height:12.5px;color:var(--muted);margin-bottom:12px}

.optin{background:var(--panel);height:210px}
.optin-head{background:var(--blue);color:var(--white);font-size:10.5px;font-weight:700;padding:12px 11px;line-height:12.5px}
.optin form{padding:10px 13px}
.optin label{display:block;font-size:10.5px;font-weight:700;margin-bottom:5px}
.optin .field{height:22px;background:var(--white);border:1px solid #ccc;margin-bottom:12px}
.optin .submit{height:37px;border-radius:7px;background:linear-gradient(#a5d870,#7cbf3a);color:var(--white);font-size:17px;font-weight:700;display:flex;align-items:center;justify-content:center;border:1px solid #79b83c}

.overview{background:var(--panel);height:276px;padding:10px 12px}
.overview h2{font-size:21px}
.steps{display:flex;align-items:center;margin:6px 0 8px}
.arrow{flex:1;height:16px}
.step-panel{background:var(--green);color:var(--white);padding:8px 8px;height:138px}
.step-panel h3{font-size:16px;font-weight:700;margin-bottom:8px}
.step-panel p{font-size:12px;line-height:15px;margin-bottom:10px}
.ticks{list-style:none;font-size:10px;line-height:12.5px;padding-left:14px}
.ticks li{display:flex;gap:6px;align-items:center}

.connect{background:var(--panel);height:31px;font-size:10.5px;font-weight:700;color:#666;padding:0 13px;display:flex;align-items:center}
.social{display:flex;justify-content:space-between;margin-top:12px}
.social .bubble{width:46px;height:46px;border-radius:50%;background:radial-gradient(circle at 40% 35%,#fafafa,#a9a9a9);display:flex;align-items:center;justify-content:center;font-size:10px;font-weight:700;color:#333}

.site-footer{border-top:2px solid #ececec;margin-top:26px;padding-top:10px}
.footer-nav{list-style:none;display:flex;font-size:10.5px;color:#444;gap:0}
.footer-nav li{display:flex;align-items:center}
.footer-nav li+li::before{content:"";width:4px;height:4px;border:1px solid #999;border-radius:50%;margin:0 20px}
.copyright{font-size:10.5px;color:#555;margin-top:16px}
</style>
</head>
<body>
<header class="site-header">
  <div class="wrap"><h1 class="site-title display">ROWAN WHITFIELD</h1></div>
</header>

<nav class="main-nav">
  <ul class="wrap">
    <li class="home">Rowan Whitfield</li>
    <li class="item">About</li>
    <li class="item" style="margin-right:38px">Speaking</li>
    <li class="item" style="margin-right:52px">Products</li>
    <li class="item" style="margin-right:45px">Programs</li>
    <li class="item">Mentoring</li>
    <li class="item">Testimonials</li>
    <li class="item">Contact</li>
  </ul>
</nav>

<section class="hero-band">
  <div class="wrap hero-row">
    <article class="intro">
      <div class="portrait-col">
        <div class="portrait" role="img" aria-label="Black and white portrait photo of Rowan Whitfield"></div>
        <div class="intro-name display">ROWAN WHITFIELD</div>
        <ul class="roles">
          <li><svg width="10" height="8" viewBox="0 0 10 8"><path d="M0 3h6V0l4 4-4 4V5H0z" fill="#fff"/></svg>Youth Expert</li>
          <li><svg width="10" height="8" viewBox="0 0 10 8"><path d="M0 3h6V0l4 4-4 4V5H0z" fill="#fff"/></svg>Motivational Speaker</li>
          <li><svg width="10" height="8" viewBox="0 0 10 8"><path d="M0 3h6V0l4 4-4 4V5H0z" fill="#fff"/></svg>Author</li>
        </ul>
      </div>
      <div class="intro-text">
        <blockquote class="quote display">"From a high school dropout to a high school valedictorian, rowan's goal is to show students how to get back on track"</blockquote>
        <p>Rowan is a youth expert- an author, youth motivational speaker and teen leader who understands the journey of many students today. The former gang member and high school drop out understands the challenges faced by students who are seeking approval and acceptance.</p>
        <p>His journey from gang member to high school teacher was long but gave empowerment and challenges students to make choices, build character and live their best life.</p>
      </div>
    </article>

    <aside class="video-card">
      <div class="player">
        <div class="frame" role="img" aria-label="Video still of Rowan speaking to a classroom of students"></div>
        <svg class="play" viewBox="0 0 44 30"><path d="M17 8l11 7-11 7z" fill="#fff"/></svg>
        <div class="side"><span></span><span></span><span></span></div>
        <div class="bar">
          <svg width="8" height="9" viewBox="0 0 8 9"><path d="M0 0l8 4.5L0 9z" fill="#fff"/></svg>
          <div class="track"><span class="time">02:18</span></div>
        </div>
      </div>
      <h3 class="video-title">Video Title</h3>
      <p class="video-desc">Lorem Ipsum is simply dummy text of the printing and typesetting industry.</p>
    </aside>
  </div>
</section>

<div class="wrap content-row">
  <div class="left-col">
    <section class="book">
      <div class="book-art" role="img" aria-label="Book and audio CD set of Life's Open Road with an open book and glasses"></div>
      <div class="book-info">
        <h2 class="display">About Book : Life's Open Road</h2>
        <div class="isbn">ISBN: 978-1-5550-3382-4</div>
        <p>Life's Open Road the inspirational story of MJ, a young man struggling with realizing his full potential. After getting into a fight at school, MJ begins to reprioritize his goals and reevaluate where he wants his life to go. He joins a leadership course initially to earn an easy A, but soon forms a bond with a mentor while on a class trip.</p>
        <p>In meeting this mentor, MJ learns of ways to improve his life and attitude, giving him a new lease on life.</p>
      </div>
    </section>

    <section class="overview">
      <h2 class="display">Overview of 5 point system</h2>
      <div class="steps">
        <svg width="48" height="48" viewBox="0 0 48 48"><circle cx="24" cy="24" r="23" fill="#ddd"/><circle cx="24" cy="24" r="19" fill="var(--green)"/><text x="24" y="33" text-anchor="middle" font-family="Arimo,Arial,sans-serif" font-weight="700" font-size="26" fill="#fff">1</text></svg>
        <svg class="arrow" viewBox="0 0 80 16" preserveAspectRatio="none"><path d="M10 8h58M63 4l5 4-5 4" stroke="#777" fill="none"/></svg>
        <svg width="48" height="48" viewBox="0 0 48 48"><circle cx="24" cy="24" r="23" fill="#ddd"/><circle cx="24" cy="24" r="19" fill="#777"/><text x="24" y="33" text-anchor="middle" font-family="Arimo,Arial,sans-serif" font-weight="700" font-size="26" fill="#fff">2</text></svg>
        <svg class="arrow" viewBox="0 0 80 16" preserveAspectRatio="none"><path d="M10 8h58M63 4l5 4-5 4" stroke="#777" fill="none"/></svg>
        <svg width="48" height="48" viewBox="0 0 48 48"><circle cx="24" cy="24" r="23" fill="#ddd"/><circle cx="24" cy="24" r="19" fill="#777"/><text x="24" y="33" text-anchor="middle" font-family="Arimo,Arial,sans-serif" font-weight="700" font-size="26" fill="#fff">3</text></svg>
        <svg class="arrow" viewBox="0 0 80 16" preserveAspectRatio="none"><path d="M10 8h58M63 4l5 4-5 4" stroke="#777" fill="none"/></svg>
        <svg width="48" height="48" viewBox="0 0 48 48"><circle cx="24" cy="24" r="23" fill="#ddd"/><circle cx="24" cy="24" r="19" fill="#777"/><text x="24" y="33" text-anchor="middle" font-family="Arimo,Arial,sans-serif" font-weight="700" font-size="26" fill="#fff">4</text></svg>
        <svg class="arrow" viewBox="0 0 80 16" preserveAspectRatio="none"><path d="M10 8h58M63 4l5 4-5 4" stroke="#777" fill="none"/></svg>
        <svg width="48" height="48" viewBox="0 0 48 48"><circle cx="24" cy="24" r="23" fill="#ddd"/><circle cx="24" cy="24" r="19" fill="#777"/><text x="24" y="33" text-anchor="middle" font-family="Arimo,Arial,sans-serif" font-weight="700" font-size="26" fill="#fff">5</text></svg>
      </div>
      <div class="step-panel">
        <h3>Honest Assessment</h3>
        <p>Like a mild cup of Harbor Bean Coffee Level 1, this exercise is just enough to get you going. Marla says this is the stage for honest assessment. What does your soul crave? Find out!</p>
        <ul class="ticks">
          <li><svg width="10" height="8" viewBox="0 0 10 8"><path d="M1 4l3 3 5-6" stroke="#fff" stroke-width="1.5" fill="none"/></svg>Praesent dignissim orci sed mi ornare sodales.</li>
          <li><svg width="10" height="8" viewBox="0 0 10 8"><path d="M1 4l3 3 5-6" stroke="#fff" stroke-width="1.5" fill="none"/></svg>Mauris porta erat ut enim cursus ut facilisis turpis molestie.</li>
          <li><svg width="10" height="8" viewBox="0 0 10 8"><path d="M1 4l3 3 5-6" stroke="#fff" stroke-width="1.5" fill="none"/></svg>Integer fringilla fringilla lorem, tempor eleifend lorem dapibus ut.</li>
        </ul>
      </div>
    </section>
  </div>

  <div class="right-col">
    <section class="optin">
      <div class="optin-head">Get Rowan's Free ebook on Helping Teens + Updates on Events &amp; Special Offers.</div>
      <form>
        <label>First Name :</label>
        <div class="field"></div>
        <label>Email Address :</label>
        <div class="field"></div>
        <div class="submit">Get me the free ebook</div>
      </form>
    </section>

    <div class="connect" style="margin-top:20px">Stay connected with Rowan Whitfield</div>
    <div class="social">
      <div class="bubble"><svg width="26" height="18" viewBox="0 0 26 18"><rect x="1" y="1" width="24" height="16" fill="#333"/><path d="M1 1l12 9 12-9" stroke="#ddd" stroke-width="1.5" fill="none"/></svg></div>
      <div class="bubble">Pals</div>
      <div class="bubble">Chirp</div>
      <div class="bubble"><svg width="22" height="22" viewBox="0 0 22 22"><circle cx="4" cy="18" r="3" fill="#333"/><path d="M2 9a11 11 0 0 1 11 11M2 3a17 17 0 0 1 17 17" stroke="#333" stroke-width="3.5" fill="none"/></svg></div>
    </div>
  </div>
</div>

<footer class="site-footer">
  <div class="wrap">
    <ul class="footer-nav">
      <li>About</li><li>Speaking</li><li>Products</li><li>Programs</li><li>Mentoring</li><li>Testimonials</li><li>Contact</li>
    </ul>
    <p class="copyright">Copyright © 2012 Rowan Whitfield. All Rights Reserved.</p>
  </div>
</footer>
</body>
</html>
```